Torvane PowerPoint Template

I have a company called Torvane, LLC and my company logo is already designed. I need a PowerPoint template that I will be using to pitch potential investors and business partners. This should be a very professional-looking template that leverages the company logo colors and really pops. The company is an AI product research and development company.

```html
<!DOCTYPE html>
<html lang="en">
<head>
<meta charset="utf-8">
<title>Torvane Pitch Deck Template</title>
<link href="https://fonts.googleapis.com/css2?family=Poppins:wght@400;500;600;700&display=swap" rel="stylesheet">
<style>
:root{
  --page:#f7f7f7;
  --slide:#232323;
  --band:#25323a;
  --wedge:#352629;
  --panel:#2c2c2c;
  --panel-teal:#223943;
  --panel-red:#3a2629;
  --blue:#1fb6f0;
  --red:#e2434b;
  --yellow:#f5c518;
  --text:#e9e9e9;
  --muted:#a4a4a4;
  --badge-text:#2a2a2a;
}
*{box-sizing:border-box;margin:0;padding:0}
html,body{width:1200px;height:1200px;overflow:hidden;background:var(--page);font-family:"Poppins",sans-serif;color:var(--text)}
.deck{position:relative;width:1200px;height:1200px}
.slide{position:absolute;width:316px;height:178px;background:var(--slide);overflow:hidden}
.slide::before{content:"";position:absolute;inset:0;background:var(--band);clip-path:polygon(48% 0,100% 0,100% 72%)}
.slide::after{content:"";position:absolute;inset:0;background:var(--wedge);clip-path:polygon(0 62%,0 100%,24% 100%)}
.slide>*{position:absolute;z-index:1}
.c1{left:66px}.c2{left:433px}.c3{left:799px}
.r1{top:16px}.r2{top:214px}.r3{top:411px}.r4{top:609px}.r5{top:807px}.r6{top:1004px}
.title{left:58px;top:27px;font-size:11px;font-weight:600;color:#fff;white-space:nowrap}
.rule{left:58px;top:43px;width:23px;height:1px;background:linear-gradient(90deg,var(--blue),var(--red))}
.brand{left:276px;top:153px;width:25px;height:13px;background:#fff;display:flex;align-items:center;justify-content:center;font-size:3.8px;font-weight:600;color:var(--badge-text)}
.tiny{font-size:2.6px;line-height:1.35;color:var(--muted)}
.lbl{font-size:3.4px;font-weight:600;color:var(--blue)}
.box{background:var(--panel);padding:5px}
.card-red{background:var(--panel-red);border-left:1px solid var(--red);padding:5px}
.card-red .lbl{color:var(--red)}
.card-teal{background:var(--panel-teal);border-left:1px solid var(--blue);padding:5px}
.outline{border:0.6px solid #2f7896;background:#262d31;padding:5px}
.bul{display:flex;gap:3px;align-items:flex-start;margin-bottom:4px}
.bul b{width:2.4px;height:2.4px;border-radius:50%;background:var(--yellow);flex:none;margin-top:.5px}
.arrow{color:var(--yellow);font-size:3px;flex:none}
.agenda b{display:inline-block;width:10px;color:var(--text);font-weight:600}
</style>
</head>
<body>
<main class="deck">

<section class="slide c1 r1">
  <h1 style="left:0;width:316px;top:28px;text-align:center;font-size:13px;line-height:1.2;font-weight:600;color:#fff">Presentation<br>Title</h1>
  <div style="left:143px;top:63px;width:30px;height:1px;background:var(--blue)"></div>
  <p style="left:0;width:316px;top:68px;text-align:center;font-size:5px;font-weight:600;color:var(--blue)">Subtitle or Tagline</p>
  <p style="left:0;width:316px;top:88px;text-align:center;font-size:3.4px;color:#cfcfcf">Presenter Name</p>
  <p style="left:0;width:316px;top:96px;text-align:center;font-size:2.8px;color:#8a8a8a">Date | Company Position</p>
  <div class="brand">Torvane</div>
</section>

<section class="slide c2 r1">
  <h2 class="title">Agenda</h2><div class="rule"></div>
  <ol class="agenda" style="left:58px;top:62px;list-style:none;font-size:3.2px;color:#d5d5d5">
    <li style="height:12.8px"><b>01</b>Company Overview</li>
    <li style="height:12.8px"><b>02</b>Problem &amp; Solution</li>
    <li style="height:12.8px"><b>03</b>Technology &amp; Innovation</li>
    <li style="height:12.8px"><b>04</b>Market Opportunity</li>
    <li style="height:12.8px"><b>05</b>Business &amp; Financial Model</li>
    <li><b>06</b>Investment Opportunity</li>
  </ol>
  <div class="brand">Torvane</div>
</section>

<section class="slide c3 r1">
  <h2 class="title">Company Overview</h2><div class="rule"></div>
  <div class="card-teal" style="left:58px;top:56px;width:148px;height:37px;background:var(--panel)">
    <p class="lbl">Our Mission</p>
    <p class="tiny" style="margin-top:4px;color:#cfcfcf">To revolutionize [industry] through cutting-edge AI solutions that solve real-world problems and create measurable value.</p>
  </div>
  <div class="card-teal" style="left:58px;top:99px;width:148px;height:48px;background:var(--panel)">
    <p class="lbl">Our Vision</p>
    <p class="tiny" style="margin-top:3px;color:#cfcfcf">To become the global leader in <span style="color:var(--yellow)">AI-driven innovation</span>, creating technologies that:</p>
    <p class="tiny" style="margin:2px 0 0 5px;font-size:2.2px">› Transform how businesses operate and compete</p>
    <p class="tiny" style="margin:1px 0 0 5px;font-size:2.2px">› Solve previously intractable problems</p>
    <p class="tiny" style="margin:1px 0 0 5px;font-size:2.2px">› Create new opportunities for growth and innovation</p>
  </div>
  <div class="brand">Torvane</div>
</section>

<section class="slide c1 r2">
  <h2 class="title">Problem Statement</h2><div class="rule"></div>
  <div class="card-red" style="left:58px;top:58px;width:148px;height:30px"><p class="lbl">Current Challenge</p><p class="tiny" style="margin-top:3px;color:#cfcfcf">Describe the primary problem or challenge that exists in the market which your company addresses</p></div>
  <div class="card-red" style="left:58px;top:93px;width:148px;height:25px"><p class="lbl">Market Gap</p><p class="tiny" style="margin-top:3px;color:#cfcfcf">Explain the specific gap in the market that creates an opportunity for your solution</p></div>
  <div class="card-red" style="left:58px;top:123px;width:148px;height:25px"><p class="lbl">Cost of Inaction</p><p class="tiny" style="margin-top:3px;color:#cfcfcf">Outline the consequences or costs that occur when this problem remains unsolved</p></div>
  <div class="brand">Torvane</div>
</section>

<section class="slide c2 r2">
  <h2 class="title">Solution Overview</h2><div class="rule"></div>
  <div role="img" aria-label="Solution visualization placeholder" style="left:58px;top:63px;width:75px;height:56px;background:#2a2a2a;border:0.5px solid #363636">
    <div style="position:absolute;left:34px;top:20px;width:6px;height:6px;border-radius:50%;background:var(--yellow)"></div>
    <p class="tiny" style="position:absolute;top:30px;width:100%;text-align:center;font-size:2px;color:#777">SOLUTION VISUALIZATION</p>
  </div>
  <div style="left:139px;top:64px;width:80px">
    <div class="bul"><b></b><p class="tiny" style="color:#cfcfcf">Describe your core solution and how it directly addresses the problem statement.</p></div>
    <div class="bul"><b></b><p class="tiny" style="color:#cfcfcf">Highlight the key differentiating features that make your solution unique.</p></div>
    <div class="bul"><b></b><p class="tiny" style="color:#cfcfcf">Explain the tangible benefits and outcomes your solution provides.</p></div>
    <div class="bul"><b></b><p class="tiny" style="color:#cfcfcf">Outline how your solution is positioned for long-term success.</p></div>
  </div>
  <div class="brand">Torvane</div>
</section>

<section class="slide c3 r2">
  <h2 class="title">Technology</h2><div class="rule"></div>
  <div class="card-teal" style="left:58px;top:59px;width:148px;height:30px"><p class="lbl">Core Technology</p><p class="tiny" style="margin-top:3px;color:#cfcfcf">Describe your proprietary technology and how it works at a high level, highlighting the <span style="color:var(--yellow)">key innovations</span> that make it unique</p></div>
  <div class="card-teal" style="left:58px;top:95px;width:148px;height:30px"><p class="lbl">Technical Advantages</p><p class="tiny" style="margin-top:3px;color:#cfcfcf">Explain the specific technical advantages your solution has over existing alternatives, with quantifiable metrics where possible.</p></div>
  <div class="card-teal" style="left:58px;top:130px;width:148px;height:30px"><p class="lbl">IP &amp; Protection</p><p class="tiny" style="margin-top:3px;color:#cfcfcf">Outline your intellectual property strategy, including patents filed or pending, trade secrets, and other competitive moats.</p></div>
  <div class="brand">Torvane</div>
</section>

<section class="slide c1 r3">
  <h2 class="title">Market Analysis</h2><div class="rule"></div>
  <div class="box" style="left:58px;top:56px;width:149px;height:78px;padding:4px">
    <p class="lbl" style="font-size:3px">Market Size &amp; Growth Projection</p>
    <svg style="position:absolute;left:4px;top:10px" width="141" height="58" viewBox="0 0 141 58">
      <g stroke="#333" stroke-width=".3"><line x1="8" y1="4" x2="140" y2="4"/><line x1="8" y1="12" x2="140" y2="12"/><line x1="8" y1="20" x2="140" y2="20"/><line x1="8" y1="28" x2="140" y2="28"/><line x1="8" y1="36" x2="140" y2="36"/><line x1="8" y1="44" x2="140" y2="44"/><line x1="8" y1="52" x2="140" y2="52"/></g>
      <path d="M10 47 L36 43 L62 38 L88 31 L114 22 L140 13 L140 52 L10 52Z" fill="#2a4a5a" opacity=".8"/>
      <polyline points="10,47 36,43 62,38 88,31 114,22 140,13" fill="none" stroke="var(--blue)" stroke-width=".6"/>
      <g fill="var(--blue)"><circle cx="10" cy="47" r=".9"/><circle cx="36" cy="43" r=".9"/><circle cx="62" cy="38" r=".9"/><circle cx="88" cy="31" r=".9"/><circle cx="114" cy="22" r=".9"/><circle cx="140" cy="13" r=".9"/></g>
      <g fill="#888" font-size="2" font-family="Poppins,sans-serif"><text x="2" y="5">60</text><text x="2" y="13">50</text><text x="2" y="21">40</text><text x="2" y="29">30</text><text x="2" y="37">20</text><text x="2" y="45">10</text><text x="3" y="53">0</text>
      <text x="8" y="57">2025</text><text x="34" y="57">2026</text><text x="60" y="57">2027</text><text x="86" y="57">2028</text><text x="112" y="57">2029</text><text x="134" y="57">2030</text></g>
    </svg>
    <p class="tiny" style="position:absolute;left:4px;bottom:4px;font-size:2px">Market size is projected to grow from $X billion in 2025 to $Y billion by 2030, representing a CAGR of Z%.</p>
  </div>
  <div class="brand">Torvane</div>
</section>

<section class="slide c2 r3">
  <h2 class="title">Competitive Landscape</h2><div class="rule"></div>
  <div style="left:95px;top:59px;width:37px;height:60px;background:var(--panel-teal)"></div>
  <svg style="left:58px;top:59px" width="150" height="62" viewBox="0 0 150 62" font-family="Poppins,sans-serif">
    <g font-size="3" font-weight="600" fill="var(--blue)"><text x="3" y="4.5">Features</text><text x="40" y="4.5">Torvane</text><text x="77" y="4.5">Competitor A</text><text x="114" y="4.5">Competitor B</text></g>
    <line x1="0" y1="7" x2="150" y2="7" stroke="var(--blue)" stroke-width=".4"/>
    <g font-size="3" fill="#cfcfcf"><text x="3" y="15">Feature 1</text><text x="3" y="25.5">Feature 2</text><text x="3" y="36">Feature 3</text><text x="3" y="46.5">Feature 4</text><text x="3" y="57">Feature 5</text></g>
    <g stroke="#3a3a3a" stroke-width=".3"><line x1="0" y1="18" x2="150" y2="18"/><line x1="0" y1="28.5" x2="150" y2="28.5"/><line x1="0" y1="39" x2="150" y2="39"/><line x1="0" y1="49.5" x2="150" y2="49.5"/></g>
    <g fill="none" stroke="var(--yellow)" stroke-width=".5"><path d="M40 14l1 1 2-2"/><path d="M40 24.5l1 1 2-2"/><path d="M40 35l1 1 2-2"/><path d="M40 45.5l1 1 2-2"/><path d="M40 56l1 1 2-2"/><path d="M77 14l1 1 2-2"/><path d="M77 45.5l1 1 2-2"/><path d="M114 24.5l1 1 2-2"/><path d="M114 45.5l1 1 2-2"/></g>
    <g stroke="var(--red)" stroke-width=".4"><path d="M77 24l1.5 1.5M78.5 24l-1.5 1.5"/><path d="M77 34.5l1.5 1.5M78.5 34.5l-1.5 1.5"/><path d="M77 55.5l1.5 1.5M78.5 55.5l-1.5 1.5"/><path d="M114 13.5l1.5 1.5M115.5 13.5l-1.5 1.5"/><path d="M114 34.5l1.5 1.5M115.5 34.5l-1.5 1.5"/><path d="M114 55.5l1.5 1.5M115.5 55.5l-1.5 1.5"/></g>
  </svg>
  <div class="brand">Torvane</div>
</section>

<section class="slide c3 r3">
  <h2 class="title">Business Model</h2><div class="rule"></div>
  <div class="outline" style="left:59px;top:59px;width:90px;height:38px"><p class="lbl" style="font-size:3px">Revenue Streams</p><p class="tiny" style="margin-top:3px;color:#cfcfcf">Outline your primary and secondary revenue sources and pricing strategy.</p></div>
  <div class="outline" style="left:153px;top:59px;width:90px;height:38px"><p class="lbl" style="font-size:3px">Cost Structure</p><p class="tiny" style="margin-top:3px;color:#cfcfcf">Summarize your major cost categories and approach to cost management.</p></div>
  <div class="outline" style="left:59px;top:104px;width:90px;height:38px"><p class="lbl" style="font-size:3px">Customer Segments</p><p class="tiny" style="margin-top:3px;color:#cfcfcf">Define your target customer groups and their specific needs.</p></div>
  <div class="outline" style="left:153px;top:104px;width:90px;height:38px"><p class="lbl" style="font-size:3px">Value Proposition</p><p class="tiny" style="margin-top:3px;color:#cfcfcf">Articulate the unique value you deliver to each customer segment.</p></div>
  <div class="brand">Torvane</div>
</section>

<section class="slide c1 r4">
  <h2 class="title">Financial Projections</h2><div class="rule"></div>
  <div style="left:58px;top:61px;width:149px;display:flex;justify-content:space-around;text-align:center">
    <div><p style="font-size:6px;font-weight:700;color:var(--yellow)">$XX.XM</p><p class="tiny" style="font-size:2.2px;margin-top:2px">Revenue Year 5</p></div>
    <div><p style="font-size:6px;font-weight:700;color:var(--yellow)">XX%</p><p class="tiny" style="font-size:2.2px;margin-top:2px">Gross Margin</p></div>
    <div><p style="font-size:6px;font-weight:700;color:var(--yellow)">XX%</p><p class="tiny" style="font-size:2.2px;margin-top:2px">YoY Growth</p></div>
  </div>
  <div class="box" style="left:58px;top:86px;width:148px;height:71px;padding:3px 4px">
    <p class="lbl" style="font-size:3px">5-Year Revenue &amp; Profit Projection</p>
    <svg style="position:absolute;left:4px;top:10px" width="140" height="58" viewBox="0 0 140 58" font-family="Poppins,sans-serif">
      <rect x="52" y="1" width="8" height="1.8" fill="var(--blue)"/><text x="61" y="2.8" font-size="1.8" fill="#888">Revenue</text>
      <rect x="72" y="1" width="8" height="1.8" fill="#c9a213"/><text x="81" y="2.8" font-size="1.8" fill="#888">Profit</text>
      <g stroke="#333" stroke-width=".3"><line x1="10" y1="8" x2="138" y2="8"/><line x1="10" y1="16" x2="138" y2="16"/><line x1="10" y1="24" x2="138" y2="24"/><line x1="10" y1="32" x2="138" y2="32"/><line x1="10" y1="40" x2="138" y2="40"/><line x1="10" y1="48" x2="138" y2="48"/></g>
      <g fill="var(--blue)"><rect x="16" y="48" width="9" height="2"/><rect x="42" y="45" width="9" height="5"/><rect x="68" y="39" width="9" height="11"/><rect x="94" y="29" width="9" height="21"/><rect x="120" y="14" width="9" height="36"/></g>
      <g fill="#c9a213"><rect x="26" y="49.3" width="9" height=".7"/><rect x="52" y="49" width="9" height="1"/><rect x="78" y="47.5" width="9" height="2.5"/><rect x="104" y="43.5" width="9" height="6.5"/><rect x="130" y="37" width="9" height="13"/></g>
      <line x1="10" y1="50" x2="138" y2="50" stroke="#555" stroke-width=".3"/>
      <g font-size="1.8" fill="#888"><text x="24" y="55">Year 1</text><text x="50" y="55">Year 2</text><text x="76" y="55">Year 3</text><text x="102" y="55">Year 4</text><text x="128" y="55">Year 5</text>
      <text x="6" y="9">35</text><text x="6" y="17">25</text><text x="6" y="25">20</text><text x="6" y="33">15</text><text x="6" y="41">10</text><text x="7" y="49">5</text></g>
    </svg>
  </div>
  <div class="brand">Torvane</div>
</section>

<section class="slide c2 r4">
  <h2 class="title">Investment Structure</h2><div class="rule"></div>
  <div class="box" style="left:58px;top:57px;width:148px;height:47px">
    <p class="lbl" style="font-size:3px;margin-bottom:3px">Funding Request</p>
    <div style="font-size:2.4px;line-height:2.75">
      <p style="display:flex;justify-content:space-between"><b>Amount Sought:</b><span style="color:var(--yellow)">$X,XXX,XXX</span></p>
      <p style="display:flex;justify-content:space-between"><b>Round Type:</b><span style="color:var(--yellow)">Series A</span></p>
      <p style="display:flex;justify-content:space-between"><b>Pre-money Valuation:</b><span style="color:var(--yellow)">$XX,XXX,XXX</span></p>
      <p style="display:flex;justify-content:space-between"><b>Equity Offered:</b><span style="color:var(--yellow)">XX%</span></p>
    </div>
  </div>
  <div class="box" style="left:58px;top:108px;width:148px;height:47px">
    <p class="lbl" style="font-size:3px;margin-bottom:3px">Use of Funds</p>
    <div style="font-size:2.4px;line-height:2.75">
      <p style="display:flex;justify-content:space-between"><b>Product Development:</b><span style="color:var(--yellow)">XX%</span></p>
      <p style="display:flex;justify-content:space-between"><b>Sales &amp; Marketing:</b><span style="color:var(--yellow)">XX%</span></p>
      <p style="display:flex;justify-content:space-between"><b>Operations:</b><span style="color:var(--yellow)">XX%</span></p>
      <p style="display:flex;justify-content:space-between"><b>Working Capital:</b><span style="color:var(--yellow)">XX%</span></p>
    </div>
  </div>
  <div class="brand">Torvane</div>
</section>

<section class="slide c3 r4">
  <h2 class="title">Team</h2><div class="rule"></div>
  <div class="outline" style="left:58px;top:60px;width:46px;height:59px;text-align:center;padding:4px 3px">
    <div role="img" aria-label="Team member portrait placeholder" style="width:14px;height:14px;margin:0 auto;border-radius:50%;background:#4a5a66"></div>
    <p style="font-size:2.8px;font-weight:600;margin-top:3px">Full Name</p><p style="font-size:2px;color:var(--blue)">Position / Title</p>
    <p class="tiny" style="font-size:1.9px;margin-top:2px">Brief professional bio highlighting key expertise and relevant experience.</p>
  </div>
  <div class="outline" style="left:109px;top:60px;width:46px;height:59px;text-align:center;padding:4px 3px">
    <div role="img" aria-label="Team member portrait placeholder" style="width:14px;height:14px;margin:0 auto;border-radius:50%;background:#4a5a66"></div>
    <p style="font-size:2.8px;font-weight:600;margin-top:3px">Full Name</p><p style="font-size:2px;color:var(--blue)">Position / Title</p>
    <p class="tiny" style="font-size:1.9px;margin-top:2px">Brief professional bio highlighting key expertise and relevant experience.</p>
  </div>
  <div class="outline" style="left:160px;top:60px;width:46px;height:59px;text-align:center;padding:4px 3px">
    <div role="img" aria-label="Team member portrait placeholder" style="width:14px;height:14px;margin:0 auto;border-radius:50%;background:#4a5a66"></div>
    <p style="font-size:2.8px;font-weight:600;margin-top:3px">Full Name</p><p style="font-size:2px;color:var(--blue)">Position / Title</p>
    <p class="tiny" style="font-size:1.9px;margin-top:2px">Brief professional bio highlighting key expertise and relevant experience.</p>
  </div>
  <div class="brand">Torvane</div>
</section>

<section class="slide c1 r5">
  <h2 class="title">Roadmap</h2><div class="rule"></div>
  <div style="left:58px;top:58px;width:150px;display:flex;justify-content:space-between;text-align:center">
    <div style="width:30px"><div style="width:5px;height:5px;border-radius:50%;background:var(--yellow);margin:0 auto"></div><p style="font-size:2.4px;color:var(--blue);margin-top:3px">Q1 2025</p><p class="tiny" style="font-size:2px">Product Development Phase 1</p></div>
    <div style="width:30px"><div style="width:5px;height:5px;border-radius:50%;background:var(--yellow);margin:0 auto"></div><p style="font-size:2.4px;color:var(--blue);margin-top:3px">Q2 2025</p><p class="tiny" style="font-size:2px">Beta Launch</p></div>
    <div style="width:30px"><div style="width:5px;height:5px;border-radius:50%;background:var(--yellow);margin:0 auto"></div><p style="font-size:2.4px;color:var(--blue);margin-top:3px">Q3 2025</p><p class="tiny" style="font-size:2px">Market Expansion</p></div>
    <div style="width:30px"><div style="width:5px;height:5px;border-radius:50%;background:var(--yellow);margin:0 auto"></div><p style="font-size:2.4px;color:var(--blue);margin-top:3px">Q4 2025</p><p class="tiny" style="font-size:2px">Series B Funding</p></div>
  </div>
  <p class="tiny" style="left:58px;top:95px;width:150px;text-align:center;font-size:2.2px;color:#777">Timeline subject to adjustment based on market conditions and development progress</p>
  <div class="brand">Torvane</div>
</section>

<section class="slide c2 r5">
  <h2 class="title">Case Studies</h2><div class="rule"></div>
  <div class="box" style="left:58px;top:60px;width:147px;height:48px;padding:5px">
    <div style="position:absolute;left:5px;top:5px;width:37px;height:37px;background:#3c4650;border:0.5px solid #4c5863"><p style="position:absolute;top:22px;width:100%;text-align:center;font-size:2.2px;color:#7fa6bf">Client Logo</p></div>
    <div style="position:absolute;left:48px;top:7px;width:94px"><p class="lbl" style="font-size:3px">Client Name / Industry</p><p class="tiny" style="font-size:2.2px;margin-top:2px;color:#cfcfcf">Brief description of the challenge faced by the client and how your solution addressed their specific needs.</p><p style="font-size:2.2px;color:var(--yellow);margin-top:2px">Result: Quantifiable outcome or improvement achieved</p></div>
  </div>
  <div class="box" style="left:58px;top:119px;width:147px;height:48px;padding:5px">
    <div style="position:absolute;left:5px;top:5px;width:37px;height:37px;background:#3c4650;border:0.5px solid #4c5863"><p style="position:absolute;top:22px;width:100%;text-align:center;font-size:2.2px;color:#7fa6bf">Client Logo</p></div>
    <div style="position:absolute;left:48px;top:7px;width:94px"><p class="lbl" style="font-size:3px">Client Name / Industry</p><p class="tiny" style="font-size:2.2px;margin-top:2px;color:#cfcfcf">Brief description of the challenge faced by the client and how your solution addressed their specific needs.</p><p style="font-size:2.2px;color:var(--yellow);margin-top:2px">Result: Quantifiable outcome or improvement achieved</p></div>
  </div>
  <div class="brand">Torvane</div>
</section>

<section class="slide c3 r5">
  <h2 class="title">Call to Action</h2><div class="rule"></div>
  <div role="img" aria-label="Next steps visualization placeholder" style="left:58px;top:59px;width:92px;height:65px;background:#2a2a2a;border:0.5px solid #363636">
    <div style="position:absolute;left:43px;top:24px;width:7px;height:7px;border-radius:50%;background:#5fa8cf"></div>
    <p style="position:absolute;top:37px;width:100%;text-align:center;font-size:2.2px;color:var(--blue)">Next Steps Visualization</p>
  </div>
  <div style="left:155px;top:62px;width:88px">
    <div class="bul"><span class="arrow">→</span><p class="tiny" style="font-size:2.2px;color:#cfcfcf">Clearly state what you're asking investors to do next (e.g., schedule follow-up meeting, review detailed materials).</p></div>
    <div class="bul" style="margin-top:5px"><span class="arrow">→</span><p class="tiny" style="font-size:2.2px;color:#cfcfcf">Summarize the key investment opportunity and unique value proposition.</p></div>
    <div class="bul" style="margin-top:5px"><span class="arrow">→</span><p class="tiny" style="font-size:2.2px;color:#cfcfcf">Emphasize time-sensitive aspects or limited availability if applicable.</p></div>
    <div class="bul" style="margin-top:5px"><span class="arrow">→</span><p class="tiny" style="font-size:2.2px;color:#cfcfcf">Reinforce confidence in your team's ability to execute and deliver results.</p></div>
  </div>
  <div class="brand">Torvane</div>
</section>

<section class="slide c1 r6">
  <h2 style="left:0;width:316px;top:40px;text-align:center;font-size:13px;font-weight:700;color:var(--blue)">Thank You</h2>
  <div style="left:136px;top:63px;width:44px;height:1px;background:linear-gradient(90deg,var(--red),var(--blue))"></div>
  <ul style="left:121px;top:72px;width:72px;height:43px;background:#1d1d1d;list-style:none;padding:5px 7px;font-size:2.3px;color:#cfcfcf;line-height:3.2">
    <li><span style="color:var(--blue);margin-right:3px">✉</span>contact@torvane.com</li>
    <li><span style="color:var(--blue);margin-right:3px">✆</span>+1 (555) 010-2040</li>
    <li><span style="color:var(--blue);margin-right:3px">◎</span>www.torvane.com</li>
    <li><span style="color:var(--blue);margin-right:3px">●</span>48 Harbor Lane, Northfield, NF 20417</li>
  </ul>
  <div class="brand">Torvane</div>
</section>

</main>
</body>
</html>
```